New automotive search style homepage

Looking for someone that can create a new homepage layout for my company. What we currently have is a little plain above the fold. We are an automotive technology company, where we take over the negotiation for customers, and perhaps we can have a design that appeals to that idea more. The current chat container is our only way to search currently, but would love to have a hybrid chat and manual search container, with the manual fields being make and model. This shouldn't have a toggle, but a seamless split view housing both features. You can see current design of our site at motorlane.net

Target Market(s)

Car buyers

Industry/Entity Type

Automotive

Number of Pages Required

1 page

Colors
0054AA
0677BA
7BADD7
CADEEF
E8F1F8

Requirements
Must have
• Above the fold is the most important

```html
<!DOCTYPE html>
<html lang="en">
<head>
<meta charset="utf-8">
<title>MotorLane – Stop Negotiating for Your Next Car</title>
<link href="https://fonts.googleapis.com/css2?family=Inter:wght@400;500;600;700;800&display=swap" rel="stylesheet">
<style>
:root{
  --navy:#151a33;
  --ink:#0f1b2d;
  --brand:#0054AA;
  --blue:#0677BA;
  --mid:#7BADD7;
  --pale:#CADEEF;
  --wash:#E8F1F8;
  --hero:#f3f7fd;
  --band:#ecf3fd;
  --grey:#5b6573;
  --line:#e3e9f1;
  --white:#ffffff;
  --star:#f5a623;
}
*{box-sizing:border-box;margin:0;padding:0}
html,body{width:1200px;height:3723px;overflow:hidden}
body{font-family:"Inter",sans-serif;color:var(--ink);background:var(--white);position:relative}
a{color:inherit;text-decoration:none}
svg{display:block}

/* nav */
.nav{position:absolute;top:0;left:0;width:1200px;height:56px;background:var(--white);border-bottom:1px solid var(--line)}
.brand{position:absolute;left:65px;top:15px;font-size:19px;font-weight:700;color:var(--ink)}
.nav-links{position:absolute;left:445px;top:17px;display:flex;gap:34px;font-size:12px;font-weight:500;color:var(--ink)}
.nav-links .active{color:var(--blue);border-bottom:2px solid var(--blue);padding-bottom:6px}
.login{position:absolute;left:965px;top:17px;font-size:13px;color:var(--grey)}
.btn-dark{position:absolute;left:1024px;top:8px;width:112px;height:34px;background:#000;color:#fff;border-radius:4px;font-size:13px;display:flex;align-items:center;justify-content:center}

/* hero */
.hero{position:absolute;top:56px;left:0;width:1200px;height:719px;background:var(--hero)}
.hero h1{position:absolute;top:54px;width:1200px;text-align:center;font-size:42px;line-height:50px;font-weight:700;letter-spacing:-.5px}
.hero h1 span{color:var(--blue);display:block}
.hero .lead{position:absolute;top:176px;left:225px;width:750px;text-align:center;font-size:15px;line-height:23px;color:var(--grey)}
.btn{position:absolute;height:47px;border-radius:4px;font-size:14px;display:flex;align-items:center;justify-content:center}
.btn-primary{background:var(--blue);color:#fff;box-shadow:0 6px 14px rgba(6,119,186,.25)}
.btn-outline{border:1px solid var(--blue);color:var(--blue);background:var(--white)}

.search-card{position:absolute;left:175px;top:337px;width:850px;height:295px;background:var(--white);border-radius:8px;box-shadow:0 10px 30px rgba(20,40,80,.10)}
.split{position:absolute;left:424px;top:0;width:1px;height:295px;background:var(--line)}
.card-title{position:absolute;font-size:20px;font-weight:600;display:flex;align-items:center;gap:8px}
.ai-title{left:32px;top:36px;color:var(--blue)}
.qs-title{left:458px;top:36px;color:var(--ink)}
.tiny-label{position:absolute;font-size:10px;color:var(--grey);letter-spacing:.5px}
.chip{position:absolute;left:33px;height:26px;padding:0 13px;border:1px solid var(--pale);border-radius:14px;font-size:10.5px;display:flex;align-items:center;background:var(--white)}
.ask{position:absolute;left:33px;top:201px;width:357px;height:60px;background:var(--hero);border-radius:4px;font-size:13px;color:var(--grey);padding:0 14px;display:flex;align-items:center;justify-content:space-between}
.select{position:absolute;top:100px;width:170px;height:60px;background:var(--hero);border-radius:4px;font-size:13px;color:var(--ink);padding:0 10px;display:flex;align-items:center;justify-content:space-between}
.search-btn{position:absolute;left:458px;top:193px;width:359px;height:60px;background:#000;color:#fff;border-radius:4px;font-size:13px;display:flex;align-items:center;justify-content:center;gap:12px}

.trust{position:absolute;top:668px;left:0;width:1200px;display:flex;justify-content:center;gap:52px;font-size:12px;font-weight:500;color:var(--grey)}
.trust div{display:flex;align-items:center;gap:7px}

/* how it works */
.how{position:absolute;top:815px;left:0;width:1200px;height:478px;background:var(--band)}
.sec-title{position:absolute;width:1200px;text-align:center;font-weight:600}
.how .sec-title{top:55px;font-size:27px}
.underline{position:absolute;top:100px;left:561px;width:78px;height:3px;background:var(--blue)}
.step{position:absolute;top:156px;width:319px;background:#f7f9fc;border:1px solid var(--line);border-radius:6px;text-align:center}
.step .ico{width:54px;height:54px;border-radius:50%;background:var(--pale);margin:34px auto 22px;display:flex;align-items:center;justify-content:center}
.step h3{font-size:20px;line-height:27px;font-weight:600;margin:0 12px 14px;white-space:nowrap}
.step p{font-size:13.5px;line-height:20px;color:var(--grey);margin:0 40px}
.arrow{position:absolute;top:268px}

/* advantage */
.eyebrow{position:absolute;left:87px;top:1390px;font-size:13px;color:var(--blue);letter-spacing:1.5px;font-weight:500}
.adv-title{position:absolute;left:87px;top:1420px;font-size:27px;font-weight:600}
.mission{position:absolute;left:941px;top:1435px;font-size:13px;color:var(--blue);display:flex;align-items:center;gap:6px}
.adv{position:absolute;top:1508px;width:242px;height:155px;background:var(--wash);border:1px solid #d6e4f4;border-radius:6px;padding:20px 20px}
.adv h4{font-size:12px;font-weight:600;margin:12px 0 8px}
.adv p{font-size:13px;line-height:20px;color:var(--grey)}

/* dark features */
.modern{position:absolute;top:1708px;left:0;width:1200px;height:646px;background:var(--navy);color:#fff}
.modern h2{position:absolute;left:71px;top:120px;font-size:26px;font-weight:600}
.feat{position:absolute;left:71px;width:500px}
.feat .fi{position:absolute;left:0;top:0;width:40px;height:40px;border-radius:4px;background:var(--blue);display:flex;align-items:center;justify-content:center}
.feat h3{margin-left:60px;font-size:20px;font-weight:500}
.feat p{margin-left:60px;margin-top:6px;font-size:13px;line-height:20px;color:#8992a8}
.photo{position:absolute;left:626px;top:105px;width:503px;height:486px;border-radius:8px;background:linear-gradient(135deg,#2b3440 0%,#4a6878 45%,#8a6a58 75%,#3a3a3a 100%)}
.savings{position:absolute;left:600px;top:511px;width:186px;height:107px;background:#dfe3e8;border-radius:6px;padding:20px 20px;color:var(--ink)}
.savings .row{display:flex;align-items:center;gap:12px;font-size:13px}
.savings .dot{width:26px;height:26px;border-radius:50%;background:#3aa7e6}
.savings .amt{color:var(--blue);font-size:14px;margin-top:10px}
.savings .small{font-size:9.5px;color:var(--grey);margin-top:2px}

/* mission quote */
.quote-mark{position:absolute;top:2442px;width:1200px;text-align:center;font-size:28px;font-weight:800;color:var(--blue)}
.quote-title{position:absolute;top:2486px;width:1200px;text-align:center;font-size:41px;font-weight:700;letter-spacing:-.5px}
.quote-text{position:absolute;top:2552px;left:235px;width:730px;text-align:center;font-size:15px;line-height:25px;color:#3d4654}

/* testimonials */
.reviews{position:absolute;top:2747px;left:0;width:1200px;height:466px;background:var(--band)}
.reviews .sec-title{top:53px;font-size:27px}
.review{position:absolute;top:140px;width:320px;height:268px;background:#f7f9fc;border-radius:6px;padding:30px 32px}
.stars{display:flex;gap:2px}
.review blockquote{font-style:italic;font-size:13px;line-height:20px;color:#2b3440;margin-top:14px;height:120px}
.person{display:flex;align-items:center;gap:14px;margin-top:10px}
.avatar{width:33px;height:33px;border-radius:50%;background:var(--pale)}
.person b{display:block;font-weight:400;font-size:13.5px}
.person span{font-size:10px;color:var(--grey)}

/* cta */
.cta{position:absolute;left:65px;top:3254px;width:1070px;height:314px;background:var(--navy);border-radius:18px;color:#fff;text-align:center}
.cta h2{margin-top:64px;font-size:40px;font-weight:700;letter-spacing:-.3px}
.cta p{margin:24px auto 0;width:580px;font-size:15px;line-height:23px;color:#6e7690}
.cta .btn{top:200px;width:204px;height:62px}
.btn-ghost{background:#2b3146;border:1px solid #4a5168;color:#fff}

/* footer */
.footer{position:absolute;top:3612px;left:0;width:1200px;height:111px;background:var(--navy);color:#fff}
.footer .fb{position:absolute;left:67px;top:40px;font-size:13px;font-weight:600}
.footer .copy{position:absolute;left:67px;top:67px;font-size:13px;color:#6e7690}
.footer nav{position:absolute;right:66px;top:55px;display:flex;gap:34px;font-size:13px;color:#6e7690}
</style>
</head>
<body>

<header class="nav">
  <a class="brand" href="#">MotorLane</a>
  <nav class="nav-links">
    <a class="active" href="#">Search</a>
    <a href="#">How It Works</a>
    <a href="#">Expert Help</a>
  </nav>
  <a class="login" href="#">Log In</a>
  <a class="btn-dark" href="#">Get Started</a>
</header>

<section class="hero">
  <h1>Stop Negotiating for Your Next Car.<span>We’ll Do It For You.</span></h1>
  <p class="lead">MotorLane combines smart vehicle search with expert negotiation technology to help you find the right car at the right price — without dealership pressure, wasted time, or hidden surprises.</p>
  <a class="btn btn-primary" style="left:405px;top:254px;width:178px" href="#">Start Your Search</a>
  <a class="btn btn-outline" style="left:603px;top:254px;width:191px" href="#">Talk to a Car Expert</a>

  <div class="search-card">
    <div class="card-title ai-title">
      <svg width="18" height="18" viewBox="0 0 24 24" fill="none" stroke="currentColor" stroke-width="2"><path d="M4 4h16v12H8l-4 4z"/></svg>AI Search
    </div>
    <div class="tiny-label" style="left:33px;top:80px">TRY ASKING</div>
    <div class="chip" style="top:100px">"Find me a reliable SUV under $35k"</div>
    <div class="chip" style="top:135px">"Best electric sedans with 300+ mile range"</div>
    <div class="ask">Ask Anything...
      <svg width="16" height="16" viewBox="0 0 24 24" fill="none" stroke="#0677BA" stroke-width="2"><path d="M3 4l18 8-18 8 3-8z"/></svg>
    </div>
    <div class="split"></div>
    <div class="card-title qs-title">
      <svg width="18" height="18" viewBox="0 0 24 24" fill="none" stroke="currentColor" stroke-width="2"><path d="M3 6h18M3 12h18M3 18h18M8 4v4M16 10v4M10 16v4"/></svg>Quick Vehicle Search
    </div>
    <div class="tiny-label" style="left:458px;top:80px">Make</div>
    <div class="tiny-label" style="left:648px;top:80px">Model</div>
    <div class="select" style="left:458px">Select Make
      <svg width="12" height="12" viewBox="0 0 24 24" fill="none" stroke="#5b6573" stroke-width="2"><path d="M6 9l6 6 6-6"/></svg></div>
    <div class="select" style="left:648px">Select Model
      <svg width="12" height="12" viewBox="0 0 24 24" fill="none" stroke="#5b6573" stroke-width="2"><path d="M6 9l6 6 6-6"/></svg></div>
    <a class="search-btn" href="#">
      <svg width="16" height="16" viewBox="0 0 24 24" fill="none" stroke="#fff" stroke-width="2.5"><circle cx="10" cy="10" r="6"/><path d="M15 15l6 6"/></svg>Search Inventory
    </a>
  </div>

  <div class="trust">
    <div><svg width="16" height="16" viewBox="0 0 24 24" fill="none" stroke="#0677BA" stroke-width="2"><circle cx="12" cy="12" r="9"/><path d="M8 12l3 3 5-6"/></svg>Thousands of Vehicles Nationwide</div>
    <div><svg width="16" height="16" viewBox="0 0 24 24" fill="none" stroke="#0677BA" stroke-width="2"><path d="M4 20h10M14 4l6 6M9 9l6 6M12 6l-6 6 4 4 6-6"/></svg>Expert Negotiators On Your Side</div>
    <div><svg width="16" height="16" viewBox="0 0 24 24" fill="none" stroke="#0677BA" stroke-width="2"><circle cx="12" cy="12" r="9"/><path d="M8 14c1 2 7 2 8 0M9 9h.01M15 9h.01"/></svg>No Dealership Pressure</div>
    <div><svg width="16" height="16" viewBox="0 0 24 24" fill="none" stroke="#0677BA" stroke-width="2"><path d="M2 12s4-7 10-7 10 7 10 7-4 7-10 7S2 12 2 12z"/><circle cx="12" cy="12" r="3"/></svg>Transparent Pricing</div>
  </div>
</section>

<section class="how">
  <h2 class="sec-title">How MotorLane Works</h2>
  <div class="underline"></div>
  <div class="step" style="left:87px;height:241px">
    <div class="ico"><svg width="24" height="24" viewBox="0 0 24 24" fill="none" stroke="#0054AA" stroke-width="2.5"><circle cx="10" cy="10" r="6"/><path d="M15 15l6 6"/></svg></div>
    <h3>1. Search Your Way</h3>
    <p>Use our AI conversational search or traditional filters to find your perfect vehicle from our massive inventory.</p>
  </div>
  <svg class="arrow" style="left:404px" width="26" height="20" viewBox="0 0 26 20" fill="none" stroke="#b3bcc8" stroke-width="2"><path d="M3 10h18M15 4l6 6-6 6"/></svg>
  <div class="step" style="left:441px;height:268px">
    <div class="ico"><svg width="24" height="24" viewBox="0 0 24 24" fill="none" stroke="#0054AA" stroke-width="2.2"><path d="M4 14v-2a8 8 0 0 1 16 0v2"/><rect x="3" y="13" width="4" height="6" rx="1"/><rect x="17" y="13" width="4" height="6" rx="1"/></svg></div>
    <h3>2. We Handle<br>Negotiations</h3>
    <p>Our expert specialists step in to negotiate the best possible price and terms directly with the dealers for you.</p>
  </div>
  <svg class="arrow" style="left:757px" width="26" height="20" viewBox="0 0 26 20" fill="none" stroke="#b3bcc8" stroke-width="2"><path d="M3 10h18M15 4l6 6-6 6"/></svg>
  <div class="step" style="left:794px;height:268px">
    <div class="ico"><svg width="24" height="24" viewBox="0 0 24 24" fill="#0054AA"><path d="M5 11l2-5h10l2 5v7h-3v-2H8v2H5z"/><circle cx="8" cy="13.5" r="1.2" fill="#CADEEF"/><circle cx="16" cy="13.5" r="1.2" fill="#CADEEF"/></svg></div>
    <h3>3. Drive Away Confidently</h3>
    <p>Review your transparent offers and pick up your car. No surprises, no hidden fees, just your new keys.</p>
  </div>
</section>

<div class="eyebrow">THE MOTORLANE ADVANTAGE</div>
<h2 class="adv-title">Why Car Buyers Choose MotorLane</h2>
<a class="mission" href="#">Learn about our mission
  <svg width="14" height="14" viewBox="0 0 24 24" fill="none" stroke="#0677BA" stroke-width="2.5"><path d="M4 12h15M13 6l6 6-6 6"/></svg></a>

<div class="adv" style="left:87px">
  <svg width="18" height="18" viewBox="0 0 24 24" fill="none" stroke="#0054AA" stroke-width="2"><circle cx="12" cy="12" r="9"/><path d="M12 7v5l3 2"/></svg>
  <h4>Save Time</h4><p>Average buyers save 12+ hours of dealership visits and research.</p>
</div>
<div class="adv" style="left:348px">
  <svg width="18" height="18" viewBox="0 0 24 24" fill="none" stroke="#0054AA" stroke-width="2"><rect x="3" y="6" width="18" height="12" rx="1"/><circle cx="12" cy="12" r="2.5"/></svg>
  <h4>Better Pricing</h4><p>Our experts secure prices on average $3,200 below sticker price.</p>
</div>
<div class="adv" style="left:610px">
  <svg width="18" height="18" viewBox="0 0 24 24" fill="none" stroke="#0054AA" stroke-width="2"><path d="M12 20c-5 0-8-4-8-8 4 0 6 2 8 5 2-3 4-5 8-5 0 4-3 8-8 8zM12 17V6M9 8l3-4 3 4"/></svg>
  <h4>Less Stress</h4><p>Eliminate the high-pressure sales environment of traditional dealerships.</p>
</div>
<div class="adv" style="left:872px">
  <svg width="18" height="18" viewBox="0 0 24 24" fill="none" stroke="#0054AA" stroke-width="2"><rect x="4" y="3" width="16" height="16" rx="1"/><circle cx="12" cy="9" r="2.5"/><path d="M8 16c1-3 7-3 8 0M4 21h16"/></svg>
  <h4>Personalized Experience</h4><p>Every search and negotiation is tailored to your specific budget and needs.</p>
</div>

<section class="modern">
  <h2>Built for Modern Car Buyers</h2>
  <div class="feat" style="top:185px">
    <div class="fi"><svg width="18" height="18" viewBox="0 0 24 24" fill="none" stroke="#fff" stroke-width="2"><path d="M12 3a7 7 0 0 0-4 12.7V20h8v-4.3A7 7 0 0 0 12 3z"/><circle cx="12" cy="10" r="2"/></svg></div>
    <h3>AI-Powered Search</h3>
    <p>Our proprietary LLM understands nuances like "best car for a growing family that fits in a small garage."</p>
  </div>
  <div class="feat" style="top:292px">
    <div class="fi"><svg width="18" height="18" viewBox="0 0 24 24" fill="#fff"><circle cx="12" cy="9" r="3"/><circle cx="5" cy="10" r="2"/><circle cx="19" cy="10" r="2"/><path d="M6 18c0-4 12-4 12 0zM1 17c0-3 4-3 5-2zM23 17c0-3-4-3-5-2z"/></svg></div>
    <h3>Real Human Negotiators</h3>
    <p>Technology meets expertise. Our agents have years of dealership experience and know all the tricks.</p>
  </div>
  <div class="feat" style="top:399px">
    <div class="fi"><svg width="18" height="18" viewBox="0 0 24 24" fill="none" stroke="#fff" stroke-width="2"><circle cx="12" cy="12" r="9"/><path d="M3 12h18M12 3c3 3 3 15 0 18M12 3c-3 3-3 15 0 18"/></svg></div>
    <h3>Nationwide Inventory</h3>
    <p>We search over 45,000 dealerships coast-to-coast to find the exact match for your preferences.</p>
  </div>
  <div class="feat" style="top:506px">
    <div class="fi"><svg width="18" height="18" viewBox="0 0 24 24" fill="none" stroke="#fff" stroke-width="2"><rect x="4" y="4" width="16" height="16" rx="1"/><path d="M8 9h3M8 13h8M8 17h8M14 8l1.5 1.5L18 7"/></svg></div>
    <h3>Transparent Process</h3>
    <p>Get a clear breakdown of every fee, tax, and discount. No hidden "documentation" surcharges.</p>
  </div>
  <div class="photo" role="img" aria-label="Photo of a technician's hand using a handheld vehicle diagnostic tablet inside a car"></div>
  <div class="savings">
    <div class="row"><span class="dot"></span>Average Savings</div>
    <div class="amt">$3,420</div>
    <div class="small">Last 30 days performance</div>
  </div>
</section>

<div class="quote-mark">99</div>
<h2 class="quote-title">Car Buying Without the Hassle</h2>
<p class="quote-text">We believe the joy of getting a new car shouldn't be overshadowed by the stress of the transaction. MotorLane was born from a simple observation: dealerships are designed to maximize profit, not your experience. We flipped the script. By placing expert negotiators and AI between you and the dealership, we ensure you always come out ahead. It's automotive expertise, democratized.</p>

<section class="reviews">
  <h2 class="sec-title">What Drivers Are Saying</h2>
  <div class="review" style="left:87px">
    <div class="stars"><svg width="84" height="16" viewBox="0 0 84 16" fill="#f5a623"><g id="s"><path d="M8 1l2.2 4.6 5 .6-3.7 3.4 1 5L8 12.2 3.5 14.6l1-5L.8 6.2l5-.6z"/></g><use href="#s" x="17"/><use href="#s" x="34"/><use href="#s" x="51"/><use href="#s" x="68"/></svg></div>
    <blockquote>"I told MotorLane I wanted a white Aster GT with specific interior colors. They found it two states away and negotiated $2,500 off the listed price. I just signed and picked it up."</blockquote>
    <div class="person"><span class="avatar"></span><div><b>Clara Whitman</b><span>Denver, CO</span></div></div>
  </div>
  <div class="review" style="left:441px">
    <div class="stars"><svg width="84" height="16" viewBox="0 0 84 16" fill="#f5a623"><use href="#s"/><use href="#s" x="17"/><use href="#s" x="34"/><use href="#s" x="51"/><use href="#s" x="68"/></svg></div>
    <blockquote>"The AI search is a game changer. It actually understood that I needed enough trunk space for two hockey bags and a stroller. Found the perfect SUV in minutes."</blockquote>
    <div class="person"><span class="avatar"></span><div><b>Owen Delgado</b><span>Atlanta, GA</span></div></div>
  </div>
  <div class="review" style="left:794px">
    <div class="stars"><svg width="84" height="16" viewBox="0 0 84 16" fill="#f5a623"><use href="#s"/><use href="#s" x="17"/><use href="#s" x="34"/><use href="#s" x="51"/><use href="#s" x="68"/></svg></div>
    <blockquote>"Negotiating with dealers is my least favorite thing. MotorLane handled the entire back-and-forth while I was at work. Professional, fast, and saved me money."</blockquote>
    <div class="person"><span class="avatar"></span><div><b>Ravi Patel</b><span>Seattle, WA</span></div></div>
  </div>
</section>

<section class="cta">
  <h2>Ready to Find Your Next Vehicle?</h2>
  <p>Join thousands of smart buyers who have skipped the dealership stress. Your perfect car and better price are just a search away.</p>
  <a class="btn btn-primary" style="left:319px" href="#">Start Searching</a>
  <a class="btn btn-ghost" style="left:543px" href="#">Get Expert Help</a>
</section>

<footer class="footer">
  <div class="fb">MotorLane</div>
  <div class="copy">© 2024 MotorLane. The Future of Automotive Negotiation.</div>
  <nav><a href="#">About Us</a><a href="#">Privacy Policy</a><a href="#">Terms of Service</a><a href="#">Contact Support</a></nav>
</footer>

</body>
</html>
```